Sales Deck For Patron Outreach Guild

We have a sales deck that we would like designing. We are looking for a fresh, vibrant design that we can use across other sales decks as well. We are an online talent business and this deck is for pitching to brands around supporting their influencer marketing endeavours. The idea is we are creating an patron outreach guild that they can join to gain key insights on a weekly basis that can help their work.

Target Market(s)

Brand managers, social media/PR teams and in house influencer marketing managers.

Industry/Entity Type

Club

Other font styles liked:
• Pier Sans

Colors
0592cd
cee9f5
85cae6
ffffff
0455a3

Requirements
Must have
• Fresh new logo for the Patron Outreach Guild as part of the deck
Nice to have
• Use the assets at our Vexamor page https://studio-48213.vexamor.com/d/pQrTn8wZkLcd/harbinger-our-brand

```html
<!DOCTYPE html>
<html lang="en">
<head>
<meta charset="utf-8">
<title>Patron Outreach Guild — Sales Deck</title>
<link href="https://fonts.googleapis.com/css2?family=Oswald:wght@400;500&family=Open+Sans:wght@400;600&display=swap" rel="stylesheet">
<style>
:root{
  --board:#c8c8c8;
  --paper:#ffffff;
  --ink:#111111;
  --muted:#555555;
  --rule:#cee9f5;
  --navy:#0455a3;
  --blue:#0592cd;
  --sky:#85cae6;
  --ice:#cee9f5;
  --white:#ffffff;
}
*{box-sizing:border-box;margin:0;padding:0}
html,body{width:1200px;height:688px;overflow:hidden;background:var(--board)}
.deck{width:1200px;height:688px;padding:8px;display:grid;grid-template-columns:repeat(4,1fr);grid-template-rows:repeat(4,1fr);gap:5px}
.slide{position:relative;overflow:hidden;background:var(--paper);font-family:"Open Sans",sans-serif;color:var(--ink)}
.abs{position:absolute}
.dot{position:absolute;top:7px;right:11px;width:5px;height:5px;border-radius:50%;background:var(--blue)}
.guild-mark{position:absolute;bottom:5px;left:0;right:0;display:flex;justify-content:center;align-items:center;gap:3px;font-size:7px;font-weight:600;color:var(--navy);white-space:nowrap}
.guild-mark i{width:7px;height:7px;border-radius:50%;background:var(--blue)}
.guild-mark.light{color:var(--white)}
.guild-mark.light i{background:var(--sky)}
.kicker{font-family:"Oswald",sans-serif;font-size:3px;letter-spacing:1px;text-transform:uppercase;text-align:center;color:var(--blue)}
.title{font-family:"Oswald",sans-serif;font-weight:400;font-size:9.5px;letter-spacing:.8px;text-transform:uppercase;text-align:center;color:var(--navy)}
.tiny{font-size:3.2px;line-height:1.35;color:var(--muted)}
.photo{position:absolute}
.frame{position:absolute;border:1.5px solid var(--white);color:var(--white);text-align:center;font-family:"Oswald",sans-serif;text-transform:uppercase;display:flex;flex-direction:column;align-items:center;justify-content:center}
.frame .kicker{color:var(--ice)}
.frame .big{font-size:18px;line-height:1.12;letter-spacing:.5px;font-weight:500}
/* cover */
.cover .photo{inset:0;background:linear-gradient(180deg,#0455a3 0%,#2f78b3 45%,#1f3f5e 72%,#0c1a2a 100%)}
.cover .frame{left:98px;top:34px;width:96px;height:95px}
.cover .big{font-size:12.5px;line-height:1.3}
.cover .guild-mark{position:static;margin-top:5px;font-family:"Open Sans",sans-serif;text-transform:none;font-size:6px}
/* quote */
.quote-box{position:absolute;left:34px;top:51px;width:226px;height:57px;border:1.5px solid var(--navy);display:flex;align-items:center;justify-content:center;text-align:center;font-family:"Oswald",sans-serif;font-size:9px;letter-spacing:1px;line-height:1.75;text-transform:uppercase;color:var(--navy)}
/* earned media */
.earned .photo{inset:0;background:linear-gradient(90deg,#0a3a66 0%,#0455a3 50%,#3d8ec2 75%,#0b3f70 100%)}
.earned .lead{left:16px;top:34px;color:var(--white);font-family:"Oswald",sans-serif;text-transform:uppercase;letter-spacing:.8px}
.earned .lead small{display:block;font-size:4.5px;margin-bottom:14px}
.earned .lead b{font-weight:400;font-size:8px;line-height:1.9;display:block}
/* insight split */
.split .photo{left:0;top:0;bottom:0;width:124px;background:radial-gradient(circle at 55% 80%,#85cae6 0%,#0592cd 30%,#0455a3 60%,#0b2440 100%)}
.split .head{left:138px;top:15px;font-family:"Oswald",sans-serif;text-transform:uppercase;letter-spacing:.6px;color:var(--navy)}
.split .head small{font-size:4.5px;letter-spacing:1.2px;display:block;color:var(--blue)}
.split .head b{font-weight:400;font-size:7px;line-height:1.25;display:block}
.block{position:absolute;width:68px}
.block .lbl{font-family:"Oswald",sans-serif;font-size:4.5px;letter-spacing:1px;margin:2px 0 1px;color:var(--navy)}
.ico{width:7px;height:7px;border:1px solid var(--blue);border-radius:50%}
/* audience */
.stat{position:absolute;font-family:"Oswald",sans-serif;font-size:11px;color:var(--blue);font-weight:500;display:flex;align-items:flex-end;gap:2px}
.box{position:absolute;border:1.5px solid var(--navy);padding:3px 4px}
.box h4{font-family:"Oswald",sans-serif;font-weight:500;font-size:4.5px;letter-spacing:.3px;margin-bottom:5px;color:var(--navy)}
.bar-row{display:flex;align-items:center;gap:3px;margin-bottom:6px;font-size:3px}
.bar-row span{width:22px}
.bar{height:6px;font-size:3px;color:var(--white);text-align:right;padding-right:2px;line-height:6px}
/* chevrons */
.step-no{position:absolute;top:45px;font-family:"Oswald",sans-serif;font-size:11px;font-weight:500;color:var(--navy)}
.step-txt{position:absolute;top:112px;width:40px}
/* pricing */
.plan{position:absolute;top:62px;width:120px;height:81px;border:1px solid var(--navy);text-align:center}
.plan h5{font-family:"Oswald",sans-serif;font-weight:400;font-size:5px;letter-spacing:.8px;padding:4px 0;border-bottom:1px solid var(--navy);color:var(--white);background:var(--blue)}
.plan p{font-size:3.3px;line-height:1.35;margin-top:4px}
/* benefits */
.benefit{position:absolute;top:59px;width:48px;text-align:center;font-family:"Oswald",sans-serif;font-size:4px;letter-spacing:1px;line-height:1.4;color:var(--navy)}
.benefit .ico{margin:0 auto 3px}
.members .photo{left:0;right:0;bottom:0;height:65px;background:linear-gradient(160deg,#cee9f5 0%,#85cae6 35%,#0592cd 65%,#0455a3 100%)}
/* partners */
.badge{position:absolute;border-radius:50%}
/* timeline */
.tl-note{position:absolute;width:40px;font-size:2.6px;line-height:1.3;color:var(--muted);text-align:center}
.tl-year{position:absolute;top:107px;font-size:2.6px;color:var(--white)}
/* get in touch */
.touch .photo{inset:0;background:linear-gradient(135deg,#0b2a4a 0%,#0455a3 35%,#85cae6 50%,#0592cd 70%,#0b2a4a 100%)}
.touch .frame{left:98px;top:34px;width:96px;height:96px}
.touch .big{font-size:16px}
/* contact */
.contact .photo{left:0;right:0;top:0;height:85px;background:linear-gradient(90deg,#0455a3 0%,#85cae6 35%,#cee9f5 55%,#85cae6 75%,#0592cd 100%)}
.contact .col{position:absolute;top:102px;width:60px;text-align:center}
.contact .col h6{font-family:"Oswald",sans-serif;font-weight:400;font-size:4.5px;letter-spacing:1.2px;margin-bottom:2px;color:var(--navy)}
.contact .footer{position:absolute;left:0;right:0;bottom:0;height:27px;background:var(--navy);display:flex;justify-content:center;align-items:center;gap:3px}
.contact .footer i{width:7px;height:7px;border:1px solid var(--white);border-radius:50%}
</style>
</head>
<body>
<main class="deck">

  <section class="slide cover">
    <div class="photo" role="img" aria-label="Dusk sky over a mountain ridge"></div>
    <div class="frame">
      <div class="kicker" style="font-size:3.5px;margin-bottom:4px">Insights</div>
      <div class="big">Always On<br>Influencer<br>Marketing</div>
      <div class="guild-mark light"><i></i>Patron Outreach Guild.</div>
    </div>
  </section>

  <section class="slide">
    <span class="dot"></span>
    <div class="quote-box">"The most credible form of advertising<br>comes straight from the people we know<br>and trust."</div>
    <div class="guild-mark"><i></i>Patron Outreach Guild.</div>
  </section>

  <section class="slide earned">
    <div class="photo" role="img" aria-label="Portrait of a businesswoman in a blue shirt against a dark wall"></div>
    <div class="abs lead"><small>"So, how can you generate more earned media?</small><b>That's where Harbinger's<br>insights come in ."</b></div>
  </section>

  <section class="slide">
    <span class="dot"></span>
    <div class="kicker abs" style="top:18px;left:0;right:0">Write here something</div>
    <div class="title abs" style="top:22px;left:0;right:0;font-size:6.5px;line-height:1.3">Influencers and consumers are<br>connected in a constant content cycle.</div>
    <svg class="abs" style="left:0;top:0" width="292" height="164" viewBox="0 0 292 164">
      <circle cx="146" cy="88" r="26" fill="var(--ice)"/>
      <g fill="none" stroke-width="10" transform="rotate(-177 146 88)">
        <circle cx="146" cy="88" r="38" stroke="var(--blue)" stroke-dasharray="53 186"/>
        <circle cx="146" cy="88" r="38" stroke="var(--sky)" stroke-dasharray="53 186" transform="rotate(90 146 88)"/>
        <circle cx="146" cy="88" r="38" stroke="var(--navy)" stroke-dasharray="53 186" transform="rotate(180 146 88)"/>
        <circle cx="146" cy="88" r="38" stroke="#4aa9d8" stroke-dasharray="53 186" transform="rotate(270 146 88)"/>
      </g>
      <circle cx="72" cy="58" r="3" fill="var(--sky)"/>
      <circle cx="67" cy="114" r="3" fill="var(--navy)"/>
      <circle cx="225" cy="104" r="3.5" fill="var(--blue)"/>
      <path d="M224 154 h6 l-1 5 h-4 z" fill="var(--navy)"/>
    </svg>
    <p class="tiny abs" style="left:30px;top:66px;width:50px">These consumers then follow the influencer to see future authentic content and trusted recommendations.</p>
    <p class="tiny abs" style="left:32px;top:124px;width:48px">Consumers engage with content, discover and share with friends and family.</p>
    <p class="tiny abs" style="left:218px;top:70px;width:52px">Influencer builds global audience through relatability &amp; shared passions.</p>
    <p class="tiny abs" style="left:218px;top:124px;width:50px">Influencer creates content featuring products the audience is invested in.</p>
  </section>

  <section class="slide split">
    <span class="dot"></span>
    <div class="photo" role="img" aria-label="Businessman holding a tablet with a glowing world network"></div>
    <div class="abs head"><small>Insight</small><b>Powered by Scoutwell,<br>solves that problem</b></div>
    <div class="block" style="left:138px;top:50px"><div class="ico"></div><div class="lbl">DATA</div><p class="tiny">We capture API data from leading platforms to discover every new piece of influential content uploaded every day and audience data from our partners to profile the creators and their audience.</p></div>
    <div class="block" style="left:212px;top:50px"><div class="ico"></div><div class="lbl">INSIGHT</div><p class="tiny">Our Scoutwell tool then processes that information to match the content to your brand, product or category to find the talent and content that is engaging your customers TODAY.</p></div>
    <div class="block" style="left:138px;top:108px"><div class="ico"></div><div class="lbl">ACTION</div><p class="tiny">A single weekly report then powers your in-house teams with the priority talent to contact with offers, product or partnership opportunities.</p></div>
    <div class="block" style="left:212px;top:108px"><div class="ico"></div><div class="lbl">RESULT</div><p class="tiny">Clients are converting an average of 30% of the leads generated by insights into earned media which drives sales on going.</p></div>
  </section>

  <section class="slide">
    <span class="dot"></span>
    <div class="kicker abs" style="top:15px;left:0;right:0">Write here something</div>
    <div class="title abs" style="top:20px;left:0;right:0">Meet your audience</div>
    <p class="tiny abs" style="top:40px;left:90px;width:112px;text-align:center;font-size:3.6px">Affluent millennial males make up the majority demographic of users.</p>
    <div class="stat" style="left:98px;top:64px">68%<svg width="7" height="15" viewBox="0 0 7 15"><circle cx="3.5" cy="2" r="2" fill="#0455a3"/><path d="M1 5h5v5H5v5H2v-5H1z" fill="#0455a3"/></svg></div>
    <div class="stat" style="left:153px;top:64px"><svg width="8" height="15" viewBox="0 0 8 15"><circle cx="4" cy="2" r="2" fill="#0455a3"/><path d="M2 5h4l2 6H6v4H2v-4H0z" fill="#0455a3"/></svg>32%</div>
    <div class="box" style="left:14px;top:82px;width:124px;height:65px">
      <h4>DEMOGRAPHICS</h4>
      <div class="bar-row"><span>● AGE 35-54</span><div class="bar" style="width:45px;background:var(--navy)">20%</div></div>
      <div class="bar-row"><span>● AGE 25-34</span><div class="bar" style="width:67px;background:var(--blue)">30%</div></div>
      <div class="bar-row"><span>● AGE 18-24</span><div class="bar" style="width:78px;background:var(--sky)">35%</div></div>
    </div>
    <div class="box" style="left:152px;top:82px;width:124px;height:65px">
      <h4>USER INCOME</h4>
      <div class="bar-row"><span>● &lt;50K</span><div class="bar" style="width:48px;background:var(--navy)">27%</div></div>
      <div class="bar-row"><span>● 50K - 99.9K</span><div class="bar" style="width:82px;background:var(--blue)">46%</div></div>
      <div class="bar-row"><span>● &gt;100K</span><div class="bar" style="width:46px;background:var(--sky)">26%</div></div>
    </div>
    <div class="guild-mark"><i></i>Patron Outreach Guild.</div>
  </section>

  <section class="slide">
    <span class="dot"></span>
    <div class="kicker abs" style="top:15px;left:0;right:0">Write here something</div>
    <div class="title abs" style="top:20px;left:0;right:0">Explosive growth</div>
    <p class="tiny abs" style="top:37px;left:40px;right:40px;text-align:center;font-size:3.6px">Since launch, membership has experienced rapid growth which continues to accelerate.</p>
    <svg class="abs" style="left:0;top:0" width="292" height="164" viewBox="0 0 292 164" font-family="Open Sans, sans-serif">
      <text x="146" y="55" font-size="4.5" text-anchor="middle" fill="#444">Series 1</text>
      <g stroke="#e6f3fa" stroke-width=".6">
        <line x1="30" y1="61" x2="266" y2="61"/><line x1="30" y1="72" x2="266" y2="72"/><line x1="30" y1="82" x2="266" y2="82"/>
        <line x1="30" y1="92" x2="266" y2="92"/><line x1="30" y1="103" x2="266" y2="103"/><line x1="30" y1="113" x2="266" y2="113"/>
      </g>
      <line x1="30" y1="123" x2="266" y2="123" stroke="#85cae6" stroke-width=".6"/>
      <g font-size="4" fill="#555" text-anchor="end">
        <text x="26" y="62">6</text><text x="26" y="73">5</text><text x="26" y="83">4</text><text x="26" y="93">3</text><text x="26" y="104">2</text><text x="26" y="114">1</text><text x="26" y="124">0</text>
      </g>
      <path d="M46 123 C58 118,66 116,76 115 S96 110,106 108 S124 96,134 83 S148 76,160 94 S176 98,190 98 S210 85,218 90 S244 76,254 71" fill="none" stroke="#0592cd" stroke-width="1"/>
      <g fill="#fff" stroke="#0455a3" stroke-width=".5">
        <circle cx="76" cy="115" r="1.3"/><circle cx="106" cy="108" r="1.3"/><circle cx="134" cy="83" r="1.3"/><circle cx="160" cy="94" r="1.3"/><circle cx="190" cy="98" r="1.3"/><circle cx="218" cy="90" r="1.3"/><circle cx="254" cy="71" r="1.3"/>
      </g>
      <rect x="64" y="90" width="44" height="9" rx="4.5" fill="#0455a3"/>
      <path d="M72 99 l3 5 l2 -5z" fill="#0455a3"/>
      <text x="86" y="96" font-size="4" fill="#fff" text-anchor="middle">GLOBAL LAUNCH</text>
      <g font-size="4" fill="#555" text-anchor="middle">
        <text x="46" y="131">MAR</text><text x="76" y="131">APR</text><text x="106" y="131">MAY</text><text x="134" y="131">JUN</text><text x="162" y="131">JUL</text><text x="190" y="131">AUG</text><text x="218" y="131">SEP</text><text x="254" y="131">OCT</text>
      </g>
    </svg>
    <div class="guild-mark"><i></i>Patron Outreach Guild.</div>
  </section>

  <section class="slide">
    <div class="photo" style="inset:0;background:radial-gradient(circle at 50% 55%,#0592cd 0%,#0455a3 55%,#06335f 100%)" role="img" aria-label="Hand touching a glowing network of social contacts"></div>
    <div class="frame" style="left:98px;top:34px;width:96px;height:96px">
      <div class="kicker" style="font-size:3.5px;margin-bottom:3px">Write here something</div>
      <div class="big">About<br>our<br>process</div>
    </div>
  </section>

  <section class="slide">
    <span class="dot"></span>
    <div class="kicker abs" style="top:17px;left:0;right:0">Harbinger</div>
    <div class="title abs" style="top:22px;left:0;right:0">Joining process</div>
    <div class="step-no" style="left:62px">01</div><div class="step-no" style="left:114px">02</div><div class="step-no" style="left:166px">03</div><div class="step-no" style="left:218px">04</div>
    <svg class="abs" style="left:0;top:0" width="292" height="164" viewBox="0 0 292 164">
      <path d="M44 65 h36 l12 17 l-12 17 h-36 l12 -17z" fill="#0455a3"/>
      <path d="M96 65 h36 l12 17 l-12 17 h-36 l12 -17z" fill="#0592cd"/>
      <path d="M148 65 h36 l12 17 l-12 17 h-36 l12 -17z" fill="#0455a3"/>
      <path d="M200 65 h36 l12 17 l-12 17 h-36 l12 -17z" fill="#0592cd"/>
      <g fill="none" stroke="#fff" stroke-width="1">
        <circle cx="74" cy="80" r="2.5"/><path d="M69 88 q5 -6 10 0"/>
        <rect x="121" y="77" width="10" height="8"/><line x1="123" y1="80" x2="129" y2="80"/>
        <path d="M172 87 l8 -8 l2 2 l-8 8 h-2z"/>
        <path d="M224 79 h4 l5 -3 v10 l-5 -3 h-4z"/>
      </g>
    </svg>
    <p class="tiny step-txt" style="left:48px">Select keyword/s or overall sector you would like to receive reports on.</p>
    <p class="tiny step-txt" style="left:100px">Add target audience demographics information to finesse search.</p>
    <p class="tiny step-txt" style="left:152px">Select minimum influencer reach if applicable.</p>
    <p class="tiny step-txt" style="left:204px">Generate first report and tweak until happy. Then receive weekly and start connecting!</p>
    <div class="guild-mark"><i></i>Patron Outreach Guild.</div>
  </section>

  <section class="slide">
    <span class="dot"></span>
    <div class="kicker abs" style="top:17px;left:0;right:0">Write here something</div>
    <div class="title abs" style="top:22px;left:0;right:0">Pricing tables</div>
    <div class="abs" style="left:18px;right:18px;top:38px;border-top:1.5px solid var(--navy)"></div>
    <div class="title abs" style="top:46px;left:0;right:0;font-size:5.5px">Insights membership from only £250 per week</div>
    <div class="plan" style="left:18px"><h5>BASIC PLAN</h5><p>£400 per week<br>3 month initial term<br>1 months notice</p><p style="margin-top:12px">Includes:<br>Weekly content tracker<br>Weekly influencer tracker</p></div>
    <div class="plan" style="left:146px;width:128px"><h5>PREMIUM PLAN</h5><p>£250 per week<br>12 month term<br>1 months notice</p><p style="margin-top:6px">Includes:<br>Weekly content tracker<br>Weekly influencer tracker<br>Monthly overview (including earned media value)<br>Rising stars tracker<br>Influencer network tracking<br>Discounts on additional services</p></div>
    <div class="guild-mark"><i></i>Patron Outreach Guild.</div>
  </section>

  <section class="slide members">
    <span class="dot"></span>
    <div class="kicker abs" style="top:17px;left:0;right:0">Write here something</div>
    <div class="title abs" style="top:22px;left:0;right:0">Members benefit</div>
    <p class="tiny abs" style="top:38px;left:80px;width:132px;text-align:center;font-size:3.4px">Members benefit from discounts on additional influencer marketing services</p>
    <div class="benefit" style="left:32px"><div class="ico"></div>Talent Deep<br>Dives</div>
    <div class="benefit" style="left:94px"><div class="ico"></div>Influencer<br>Tracking</div>
    <div class="benefit" style="left:156px"><div class="ico"></div>Outreach<br>Program</div>
    <div class="benefit" style="left:218px"><div class="ico"></div>Full Campaign<br>Management</div>
    <div class="photo" role="img" aria-label="View up a glass office tower"></div>
  </section>

  <section class="slide">
    <span class="dot"></span>
    <div class="kicker abs" style="top:17px;left:0;right:0">Write here something</div>
    <div class="title abs" style="top:22px;left:0;right:0">Our partners</div>
    <div class="abs" style="left:52px;right:52px;top:84px;border-top:1px solid var(--rule)"></div>
    <div class="abs" style="left:120px;top:60px;height:48px;border-left:1px solid var(--rule)"></div>
    <div class="abs" style="left:172px;top:60px;height:48px;border-left:1px solid var(--rule)"></div>
    <div class="abs" style="left:80px;top:70px;width:18px;height:4px;background:var(--navy)"></div>
    <div class="abs" style="left:138px;top:70px;width:18px;height:4px;background:var(--blue)"></div>
    <div class="abs" style="left:190px;top:70px;width:26px;height:4px;background:var(--navy)"></div>
    <div class="abs" style="left:82px;top:94px;width:14px;height:5px;background:var(--blue)"></div>
    <div class="abs" style="left:140px;top:92px;width:14px;height:8px;background:var(--sky)"></div>
    <div class="abs" style="left:194px;top:93px;width:16px;height:6px;background:var(--navy)"></div>
    <div class="guild-mark"><i></i>Patron Outreach Guild.</div>
  </section>

  <section class="slide">
    <span class="dot"></span>
    <div class="kicker abs" style="top:17px;left:0;right:0">Write here something</div>
    <div class="title abs" style="top:22px;left:0;right:0">Our partners</div>
    <div class="abs" style="left:54px;right:54px;top:91px;border-top:1px solid var(--rule)"></div>
    <div class="abs" style="left:121px;top:68px;height:48px;border-left:1px solid var(--rule)"></div>
    <div class="abs" style="left:171px;top:68px;height:48px;border-left:1px solid var(--rule)"></div>
    <div class="badge" style="left:92px;top:76px;width:9px;height:9px;background:var(--blue)"></div>
    <div class="badge" style="left:142px;top:76px;width:10px;height:10px;background:var(--navy)"></div>
    <div class="badge" style="left:193px;top:76px;width:9px;height:9px;background:var(--sky)"></div>
    <div class="badge" style="left:92px;top:97px;width:9px;height:9px;background:var(--navy)"></div>
    <div class="badge" style="left:142px;top:97px;width:10px;height:10px;background:var(--sky)"></div>
    <div class="abs" style="left:193px;top:97px;width:10px;height:10px;background:var(--blue)"></div>
    <div class="guild-mark"><i></i>Patron Outreach Guild.</div>
  </section>

  <section class="slide">
    <span class="dot"></span>
    <div class="kicker abs" style="top:17px;left:0;right:0">Harbinger</div>
    <div class="title abs" style="top:22px;left:0;right:0;font-size:6.5px">Leaders in finding online talent</div>
    <svg class="abs" style="left:0;top:0" width="292" height="164" viewBox="0 0 292 164">
      <rect x="3" y="103" width="282" height="7" fill="#0455a3"/>
      <path d="M282 99 l8 7.5 l-8 7.5z" fill="#0455a3"/>
      <g stroke="#85cae6" stroke-width=".4">
        <line x1="60" y1="64" x2="60" y2="103"/><line x1="32" y1="80" x2="32" y2="103"/><line x1="98" y1="92" x2="98" y2="103"/>
        <line x1="138" y1="64" x2="138" y2="103"/><line x1="190" y1="86" x2="190" y2="103"/><line x1="246" y1="64" x2="246" y2="103"/>
        <line x1="32" y1="110" x2="32" y2="126"/><line x1="90" y1="110" x2="90" y2="124"/><line x1="140" y1="110" x2="140" y2="128"/>
        <line x1="200" y1="110" x2="200" y2="124"/><line x1="248" y1="110" x2="248" y2="126"/>
      </g>
      <text x="6" y="108.5" font-size="3.6" fill="#fff" font-family="Open Sans, sans-serif">Harbinger</text>
    </svg>
    <span class="tl-year" style="left:58px">2015</span><span class="tl-year" style="left:130px">2016</span><span class="tl-year" style="left:200px">2017</span>
    <p class="tl-note" style="left:40px;top:44px">Major record label and venture builders invest in Harbinger following successful tech demo</p>
    <p class="tl-note" style="left:12px;top:62px">Label president connects with Harbinger founders and trials early reports</p>
    <p class="tl-note" style="left:78px;top:74px">Harbinger extends tech capability through data partnerships and launches a brand solution</p>
    <p class="tl-note" style="left:118px;top:44px">Tech discovers a breakout singer before the talent shows and helps him become a top artist</p>
    <p class="tl-note" style="left:170px;top:68px">Harbinger launches its first influencer campaign exclusively using talent selection</p>
    <p class="tl-note" style="left:226px;top:44px">National press features Harbinger and how it is changing talent discovery</p>
    <p class="tl-note" style="left:12px;top:127px">Harbinger develops tech to discover music talent by tracking online video data</p>
    <p class="tl-note" style="left:70px;top:125px">A major music label begins working with Harbinger to find the next stars</p>
    <p class="tl-note" style="left:120px;top:129px">Brand division delivers campaigns across the globe for leading broadcasters and retailers</p>
    <p class="tl-note" style="left:180px;top:125px">Harbinger begins to develop machine learning and launches its talent platform</p>
    <p class="tl-note" style="left:228px;top:127px">Harbinger celebrates its first best seller in books and launches insights</p>
  </section>

  <section class="slide touch">
    <div class="photo" role="img" aria-label="Upward view of glass skyscrapers"></div>
    <div class="frame">
      <div class="kicker" style="font-size:3.5px;margin-bottom:3px">Write here something</div>
      <div class="big">Get<br>in<br>touch</div>
    </div>
  </section>

  <section class="slide contact">
    <div class="photo" role="img" aria-label="Hand holding a smartphone on a busy blurred street"></div>
    <div class="col" style="left:36px"><h6>LOCATION</h6><p class="tiny">Add your street, town and postcode here depending on the office</p></div>
    <div class="col" style="left:116px"><h6>OUR HOURS</h6><p class="tiny">Monday to Friday from nine until six depending on the team</p></div>
    <div class="col" style="left:196px"><h6>CONTACT US</h6><p class="tiny">Add your phone and email details here depending on the desk</p></div>
    <div class="footer"><i></i><i></i><i></i><i></i></div>
  </section>

</main>
</body>
</html>
```